Business Card for Start Up Real Estate Company

We need a business card designed for a new real estate company called Belvanta. We plan on improving the experience of real estate transactions for both consumers and agents by using current and evolving technology. We would like to see designs that use our existing logo (attached). Please use a primarily white or light colored background. The final design should communicate technology, sophistication and customer service. Thank you...

Industry/Entity Type

Real Estate

Requirements
Must have
• Primarily white or light colored background
Nice to have
• Isolated A from our logo used as part of the design
Should not have
• Pictures, especially of houses

```html
<!DOCTYPE html>
<html lang="en">
<head>
<meta charset="utf-8">
<title>Belvanta Business Card</title>
<link rel="stylesheet" href="https://fonts.googleapis.com/css2?family=Cabin:wght@400;500;600&display=swap">
<style>
  :root {
    --page-bg: #ece9e4;
    --card-bg: #ffffff;
    --brand-blue: #135a96;
    --brand-red: #e51f3e;
    --card-shadow: rgba(60, 45, 20, 0.35);
  }
  html, body {
    margin: 0;
    padding: 0;
    width: 1200px;
    height: 1000px;
    overflow: hidden;
    background: var(--page-bg);
    font-family: "Cabin", "Helvetica Neue", Arial, sans-serif;
  }
  .canvas {
    position: relative;
    width: 1200px;
    height: 1000px;
  }
  .card {
    position: absolute;
    left: 445px;
    top: 230px;
    width: 330px;
    height: 506px;
    background: var(--card-bg);
    border-radius: 16px;
    box-shadow: 2px 3px 6px var(--card-shadow);
    overflow: hidden;
  }
  .brand-name {
    position: absolute;
    left: 0;
    right: 0;
    top: 44px;
    text-align: center;
    font-size: 36px;
    font-weight: 500;
    letter-spacing: 1px;
    color: var(--brand-blue);
    line-height: 1;
  }
  .name-marker {
    position: absolute;
    left: 0;
    top: 166px;
    width: 17px;
    height: 38px;
    background: var(--brand-red);
  }
  .person-name {
    position: absolute;
    left: 36px;
    top: 163px;
    margin: 0;
    font-size: 19px;
    font-weight: 400;
    color: var(--brand-blue);
  }
  .job-title {
    position: absolute;
    left: 39px;
    top: 192px;
    margin: 0;
    font-size: 13px;
    color: var(--brand-red);
  }
  .contact {
    position: absolute;
    left: 34px;
    top: 314px;
    margin: 0;
    padding: 0;
    list-style: none;
    font-size: 11.5px;
    line-height: 18px;
    color: var(--brand-blue);
  }
  .contact li {
    position: relative;
    padding-left: 22px;
  }
  .contact .address { margin-bottom: 20px; }
  .contact .company { font-weight: 600; }
  .contact svg {
    position: absolute;
    left: 0;
    top: 2px;
    width: 13px;
    height: 13px;
    fill: none;
    stroke: var(--brand-red);
    stroke-width: 1.2;
  }
</style>
</head>
<body>
<div class="canvas">
  <div class="card">
    <div class="brand-name">BELVANTA</div>

    <div class="name-marker"></div>
    <h1 class="person-name">Firstname J.Lastname</h1>
    <p class="job-title">Your job Title</p>

    <ul class="contact">
      <li class="address">
        <svg viewBox="0 0 14 14"><path d="M7 13 C4 9.5 2.8 7.3 2.8 5.2 A4.2 4.2 0 0 1 11.2 5.2 C11.2 7.3 10 9.5 7 13Z"/><circle cx="7" cy="5.2" r="1.6"/></svg>
        <span class="company">BELVANTA</span> Real estate<br>
        1236 Your Street Adress, Town,<br>
        State , Country, Zip 90210
      </li>
      <li>
        <svg viewBox="0 0 14 14"><path d="M3 1.5 L5.2 1.5 L6 4.5 L4.6 5.6 C5.4 7.4 6.6 8.6 8.4 9.4 L9.5 8 L12.5 8.8 L12.5 11 C12.5 12 11.7 12.6 10.8 12.5 C6 12 2 8 1.5 3.2 C1.4 2.3 2 1.5 3 1.5Z"/></svg>
        +093 555 0142
      </li>
      <li>
        <svg viewBox="0 0 14 14"><rect x="1.5" y="3" width="11" height="8"/><path d="M1.5 3 L7 7.5 L12.5 3"/></svg>
        mail@belvantahomes.com
      </li>
      <li>
        <svg viewBox="0 0 14 14"><circle cx="7" cy="5.5" r="4.2"/><path d="M5.3 9.5 L5.3 12 L8.7 12 L8.7 9.5 M5.3 11 L8.7 11"/></svg>
        www.belvantahomes.com
      </li>
    </ul>
  </div>
</div>
</body>
</html>
```